8 1/2 x 11 Flyer mailer for Window Envelope.

I need a flyer/mailer advertisement for a 9x12 window envelope. The front page needs to have text from a Word document which I will be uploading. A colorful header with our logo, phone number, fax number, mailing address, and website need to be at the top.

Just below the header needs to be an open white space where we can print addresses for the bulk mailing. The White space is from the Date on word docs uploaded all the way down to the Dear etc. It needs to be white and open f so that we can run the flyer through a printer to print the address, date, and dear mr: specifically and most importantly that the address may appear through the window.

General pictures of the lawyers and company colors on the front page with provided text.

On the back of the flyer we would like full color with a map to our office, preferably like the one we have on our website, along with practice areas and the info from our website. Including the about us portion, and the excerpts from the front of our website

www.DesertDefenseCounsel.example

The Back of the flyer can be the same for each of the 5 flyers, but the text on the front needs to reflect the text in the five word documents I have uploaded.
Updates

To be more specific for the Flyer.  The flyer should be like a letterhead on the front, with the text from the letter I am currently using.  With a footer as well with our website address and phone number at the bottom.

The back of the flyer should look like the half page flyer I posted with the design.

```html
<!DOCTYPE html>
<html lang="en">
<head>
<meta charset="utf-8">
<title>Desert Defense Counsel – Client Letter</title>
<link rel="stylesheet" href="https://fonts.googleapis.com/css2?family=Arimo:wght@400;700&family=Cormorant+Garamond:wght@500&display=swap">
<style>
  :root {
    --ink: #3a3a3a;
    --ink-strong: #1f1f1f;
    --paper: #ffffff;
    --band: #0c0c0c;
    --band-text: #ffffff;
    --ribbon: #8d8f93;
    --photo-light: #d9dde2;
    --photo-mid: #9aa3ad;
    --photo-dark: #4c5560;
  }
  * { margin: 0; padding: 0; box-sizing: border-box; }
  html, body { width: 945px; height: 1200px; overflow: hidden; background: var(--paper); }
  .flyer {
    position: relative;
    width: 945px;
    height: 1200px;
    background: var(--paper);
    font-family: "Arimo", Arial, sans-serif;
    color: var(--ink);
  }
  .hero { position: absolute; top: 0; left: 0; width: 945px; height: 600px; display: block; }
  .letter {
    position: absolute;
    top: 522px;
    left: 60px;
    width: 832px;
    font-size: 12.4px;
    line-height: 18px;
  }
  .letter p { margin-bottom: 8px; }
  .letter .date { color: var(--ink-strong); font-size: 13px; margin-bottom: 9px; }
  .letter .to { margin-bottom: 9px; line-height: 17px; }
  .letter .to .name { color: var(--ink-strong); font-size: 13px; }
  .letter .salutation { margin-bottom: 7px; }
  .letter strong { color: var(--ink-strong); font-weight: 400; font-size: 13.2px; }
  .questions {
    list-style: none;
    margin: 3px 0 7px 258px;
    font-size: 13.6px;
    color: var(--ink-strong);
  }
  .questions li { margin-bottom: 8px; position: relative; padding-left: 13px; }
  .questions li:last-child { margin-bottom: 0; }
  .questions li::before { content: "•"; position: absolute; left: 0; }
  .signoff p { margin-bottom: 7px; color: var(--ink-strong); font-size: 13px; }
  .footer-band {
    position: absolute;
    left: 0; bottom: 0;
    width: 945px; height: 104px;
    background: var(--band);
    color: var(--band-text);
  }
  .brand-mark {
    position: absolute; left: 38px; top: 14px;
    width: 76px; height: 76px;
    border: 2px solid var(--band-text);
    border-radius: 50%;
  }
  .brand-name {
    position: absolute; left: 137px; top: 21px;
    font-family: "Cormorant Garamond", Georgia, serif;
    font-weight: 500;
    font-size: 28px;
    line-height: 1.06;
    letter-spacing: 1.2px;
    text-transform: uppercase;
  }
  .contact { position: absolute; left: 515px; top: 24px; font-size: 14px; line-height: 18px; white-space: nowrap; }
  .contact b { font-weight: 700; }
  .address { position: absolute; left: 805px; top: 24px; font-size: 14px; line-height: 18px; white-space: nowrap; }
</style>
</head>
<body>
<main class="flyer">
  <svg class="hero" viewBox="0 0 945 600">
    <defs>
      <linearGradient id="photoTone" x1="0" y1="0" x2="1" y2="1">
        <stop offset="0" stop-color="var(--photo-light)"/>
        <stop offset="0.55" stop-color="var(--photo-mid)"/>
        <stop offset="1" stop-color="var(--photo-dark)"/>
      </linearGradient>
      <linearGradient id="ribbonTone" x1="0" y1="0" x2="1" y2="0">
        <stop offset="0" stop-color="#ffffff"/>
        <stop offset="0.5" stop-color="var(--ribbon)"/>
        <stop offset="1" stop-color="#6f7176"/>
      </linearGradient>
    </defs>
    <rect x="0" y="0" width="945" height="590" fill="url(#photoTone)" role="img" aria-label="Photo of two attorneys meeting with a client at a laptop in an office"/>
    <path d="M0,488 L530,488 C585,488 590,582 650,582 L945,582 L945,600 L0,600 Z" fill="url(#ribbonTone)"/>
    <path d="M0,498 L520,498 C575,498 580,596 640,596 L945,596 L945,600 L0,600 Z" fill="var(--paper)"/>
  </svg>

  <section class="letter">
    <p class="date">December 23, 2013</p>
    <p class="to">To,<br><span class="name">Abc</span></p>
    <p class="salutation">Dear «4»:</p>
    <p>Public records show that you were recently and unfortunately charged with <strong>Domestic Violence</strong>. It is very important that you know your rights and obligations in this matter and that you receive the best possible legal representation. Our Criminal Defense Attorneys and Legal Team have significant experience defending domestic violence cases. <strong>New Mexico Domestic Violence laws provide for serious and mandatory criminal penalties.</strong> Some important questions you need answered are:</p>
    <ul class="questions">
      <li>What are the maximum possible fines and penalties?</li>
      <li>Is there a No Contact order against me, and what does it mean?</li>
      <li>What are my legal rights?</li>
    </ul>
    <p><strong>IMPORTANT: You have only 10 days from the date you are arraigned to excuse the Judge assigned to your case pursuant to NMSA 30-3-9</strong>. This decision alone may make a difference in the outcome of your case. We have enclosed a Notice of Excusal form that you may submit to the Court. Notice of Excusal forms can be filed during business hours at the Criminal Settings window at City Court, 750 Cedar Plaza NW, Sandstone, NM 87199. If you contact our office within 5 days from the date your case was filed we will guarantee to represent you at any pending Temporary Restraining Order Hearing related to your case for no additional charge.</p>
    <p>Call 555-0142 for a FREE EVALUATION of your case. You will need all paperwork regarding your case for a proper evaluation. In reviewing the individual facts of your case, we will determine whether the officers who made contact with you followed the proper procedure. We will also help you examine all of your options and determine whether the judge assigned to your case should be excused.</p>
    <p>Weare members of the State Criminal Defense Bar Network, and we have more than 23 years combined experience in defending Domestic Violence cases. Our fees are designed to be affordable to you. We will meet with you at your convenience.</p>
    <div class="signoff">
      <p>Sincerely,</p>
      <p>Desert Defense Counsel</p>
      <p>Attorneys at Law</p>
    </div>
  </section>

  <footer class="footer-band">
    <div class="brand-mark"></div>
    <div class="brand-name">Desert Defense<br>Counsel</div>
    <div class="contact">
      <div><b>Phone</b> : (505) 555-0142</div>
      <div><b>Fax</b> : (505) 555-0178</div>
      <div><b>Web</b> : www.DesertDefenseCounsel.example</div>
    </div>
    <div class="address">2140 Mesa Ave.<br>NW Sandstone<br>NM 87199</div>
  </footer>
</main>
</body>
</html>
```